Berrocal Tizón Law Firm for Small and Medium Business: Website

We need a web design that includes coding for the Wix platform, for a new company based in Santiago, Chile, called Berrocal Tizón, Abogados y Consultores. The company is essentially a law firm, with additional advisory services in accounting, tax management and finance. The main target of the company are founders, CEOs or C-level executives of small or medium companies based in Chile.
The main menu of the web page must have the following tab options:
- Home - About us - Services – How we work -Blog – FAQ -Contact
Our main services are:

1.- Commercial and corporate law advisory
2.- Legal defense in civil, criminal, labor and family matters (litigation and arbitration)
3.- Bankruptcy and reorganization of companies
4.- Collection and recovery of assets
5.- Asset protection
6.- Financial and tax advice

We want to highlight the following services:

-Bankruptcy and reorganization of companies
-Judicial defense in civil matters
-Financial and tax advice

In addition to these services, the following will be offered:
-Lawyer at your home for special cases
-Half hour free consultation
-Monthly service packages

The final design should communicate confidence, business savvy and high execution standards and quality.

Target Market(s)

The main target of the company are founders, CEOs or C-level executives of small or medium companies based in Chile.

Industry/Entity Type

Legal industry

Coding

Number of Pages Required

5+ page

Font styles to use
Serif

Requirements
Must have
• 1. Big banners para destacar los siguientes servicios: -Bankruptcy and reorganization of companies -Judicial defense in civil matters -Financial and tax advice 2. Call to action para agendar consulta legal. 3. Destacar los siguientes servicios: -Lawyer at your home for special cases -Half hour free consultation -Monthly service packages 3. Página para explicar cómo se cobra (precios transparentes): ver el siguiente sitio web: https://www.brookvanelegal.example/how 4. Links to Facebook, Instagram and Linkedin 5. Connection to Whatsapp.
Should not have
• Look old fashioned

```html
<!DOCTYPE html>
<html lang="en">
<head>
<meta charset="utf-8">
<title>Berrocal Tizón — Abogados y Consultores</title>
<link href="https://fonts.googleapis.com/css2?family=Orbitron:wght@500;700&family=Roboto:wght@400;500;700&display=swap" rel="stylesheet">
<style>
:root{
  --dark:#15231f;
  --gold:#a98d21;
  --gold-light:#d1bb36;
  --gold-deep:#8a7418;
  --text:#444;
  --muted:#5b5b5b;
  --white:#fff;
}
*{margin:0;padding:0;box-sizing:border-box}
html,body{width:1200px;height:3404px;overflow:hidden}
body{font-family:Roboto,Arial,sans-serif;color:var(--text);background:#fff;position:relative}
.display{font-family:Orbitron,sans-serif;letter-spacing:1px}
a{text-decoration:none;color:inherit}

/* header */
.site-header{position:absolute;top:0;left:0;width:1200px;height:122px;background:var(--dark);border-bottom:4px solid var(--gold-light)}
.brand{position:absolute;left:111px;top:34px;display:flex;align-items:center;gap:10px}
.brand-mark{width:48px;height:48px;background:var(--gold)}
.brand-name{font-family:Orbitron,sans-serif;font-weight:500;font-size:27px;color:var(--gold-light);line-height:1}
.brand-sub{font-family:Orbitron,sans-serif;font-size:8px;color:var(--gold-light);letter-spacing:1.5px;margin-top:4px;padding-left:22px}
.main-nav{position:absolute;right:110px;top:51px;display:flex;gap:30px}
.main-nav a{font-family:Orbitron,sans-serif;font-size:13px;color:var(--white);font-weight:500}

/* hero */
.hero{position:absolute;top:126px;left:0;width:1200px;height:694px;background:linear-gradient(100deg,#3a2e26 0%,#5b4a3c 35%,#6e625a 60%,#3b3330 100%)}
.hero-shade{position:absolute;inset:0;background:rgba(0,0,0,.28)}
.hero-title{position:absolute;top:310px;width:100%;text-align:center;color:var(--white)}
.hero-title h1{font-family:Orbitron,sans-serif;font-weight:500;font-size:50px;letter-spacing:3px;line-height:1}
.hero-title h2{font-family:Orbitron,sans-serif;font-weight:500;font-size:38px;letter-spacing:2px;margin-top:12px}
.hero-offers{position:absolute;top:448px;left:0;width:100%;display:flex;justify-content:center;gap:6px}
.hero-offers span{display:block;padding:0 15px;height:46px;line-height:46px;font-size:13px;font-weight:500;color:var(--white);background:var(--dark);border-radius:2px}
.hero-offers span.accent{background:var(--gold)}

/* welcome */
.welcome{position:absolute;top:860px;left:0;width:1200px;text-align:center}
.section-title{font-family:Orbitron,sans-serif;font-weight:700;font-size:32px;color:var(--dark);letter-spacing:1px}
.section-title em{font-style:normal;color:var(--gold)}
.welcome p{width:720px;margin:22px auto 0;font-family:Arial,sans-serif;font-size:13.5px;line-height:26px;color:var(--text)}
.highlights{position:absolute;top:1051px;left:0;width:1200px;height:316px}
.circle{position:absolute;border-radius:50%;display:flex;flex-direction:column;align-items:center;justify-content:center;text-align:center;color:var(--white);font-family:Orbitron,sans-serif;font-size:17px;line-height:28px;letter-spacing:1px}
.circle svg{margin-bottom:22px}
.circle.dark{background:var(--dark);width:286px;height:286px;top:14px}
.circle.left{left:195px}
.circle.right{left:717px}
.circle.gold{left:440px;top:0;width:312px;height:312px;background:radial-gradient(circle at 40% 30%,#d8c234,#a58c20 70%,#8c761a);z-index:2}

/* services */
.services{position:absolute;top:1440px;left:0;width:1200px;height:523px;background:linear-gradient(120deg,#a88d1f,#b79b25 50%,#a5891d)}
.services .section-title{position:absolute;top:50px;width:100%;text-align:center;color:var(--white)}
.rule{display:block;width:46px;height:3px;background:var(--dark);margin:0 auto}
.services .rule{position:absolute;top:103px;left:577px;background:var(--white)}
.service{position:absolute;width:440px}
.service .icon{position:absolute;left:0;top:0;width:124px;height:124px;border-radius:50%;background:var(--dark);display:flex;align-items:center;justify-content:center}
.service .body{position:absolute;left:151px;top:0;width:300px;color:var(--white)}
.service h3{font-size:17px;font-weight:700;line-height:27px}
.service p{font-family:Arial,sans-serif;font-size:13.5px;line-height:26px;margin-top:6px;opacity:.95}

/* blog */
.blog{position:absolute;top:1963px;left:0;width:1200px;height:614px}
.blog .section-title{position:absolute;top:50px;width:100%;text-align:center}
.blog .rule{position:absolute;top:102px;left:577px}
.post{position:absolute;top:138px;width:312px;height:397px}
.post .photo{width:312px;height:229px;background:linear-gradient(135deg,#6c6b69,#b6b2aa 60%,#e3e0da)}
.post .card{position:absolute;left:16px;top:199px;width:281px;height:198px;background:#fff;box-shadow:0 1px 4px rgba(0,0,0,.18);text-align:center;padding-top:30px}
.post .date{font-family:Orbitron,sans-serif;font-size:15px;color:var(--gold);font-weight:700}
.post h4{font-family:Orbitron,sans-serif;font-size:14px;color:var(--dark);margin-top:14px;font-weight:700}
.post p{font-family:Arial,sans-serif;font-size:13px;line-height:23px;color:var(--muted);margin:18px auto 0;width:250px}

/* how we work */
.how{position:absolute;top:2577px;left:0;width:1200px;height:480px;background:#f4f4f4}
.how .photo{position:absolute;left:0;top:0;width:588px;height:480px;background:linear-gradient(110deg,#3a3f4b,#8c8f94 40%,#cbc6bf 70%,#7b6f63)}
.how .content{position:absolute;left:645px;top:52px;width:445px}
.how .rule{margin:18px 0 0;width:48px}
.how p{font-family:Arial,sans-serif;font-size:13.5px;line-height:26px;color:var(--muted);margin-top:26px;text-align:justify}
.btn{display:inline-block;margin-top:26px;width:159px;height:53px;line-height:53px;text-align:center;background:var(--gold);color:var(--white);font-family:Orbitron,sans-serif;font-size:13px}

/* footer */
.site-footer{position:absolute;top:3057px;left:0;width:1200px;height:347px;background:var(--dark);color:var(--white)}
.site-footer .brand{left:447px;top:56px}
.footer-nav{position:absolute;top:148px;width:100%;display:flex;justify-content:center;gap:42px}
.footer-nav a{font-family:Orbitron,sans-serif;font-size:14px}
.social{position:absolute;top:197px;width:100%;display:flex;justify-content:center;gap:7px}
.social span{width:36px;height:36px;border:1.5px solid var(--white);border-radius:50%}
.copyright{position:absolute;top:265px;width:100%;text-align:center;font-family:Arial,sans-serif;font-size:14px}
</style>
</head>
<body>

<header class="site-header">
  <div class="brand">
    <div class="brand-mark"></div>
    <div><div class="brand-name">Berrocal Tizón</div><div class="brand-sub">ABOGADOS Y CONSULTORES</div></div>
  </div>
  <nav class="main-nav">
    <a href="#">HOME</a><a href="#">ABOUT US</a><a href="#">SERVICES</a><a href="#">HOW WE WORK</a><a href="#">BLOG</a><a href="#">FAQ</a><a href="#">CONTACT</a>
  </nav>
</header>

<section class="hero" role="img" aria-label="Smiling lawyer in shirt and tie at a boardroom table with colleagues in a meeting behind him">
  <div class="hero-shade"></div>
  <div class="hero-title">
    <h1>BERROCAL TIZÓN</h1>
    <h2>ABOGADOS Y CONSULTORES</h2>
  </div>
  <div class="hero-offers">
    <span>HALF HOUR FREE CONSULTATION</span>
    <span class="accent">LAWYER AT YOUR HOME FOR SPECIAL CASES</span>
    <span>MONTHLY SERVICE PACKAGES</span>
  </div>
</section>

<section class="welcome">
  <h2 class="section-title">WELCOME TO <em>BERROCAL TIZÓN</em></h2>
  <p>Sed ut perspiciatis unde omnis iste natus error sit voluptatem accusantium doloremque laudantium, totam rem aperiam, eaque ipsa quae ab illo inventore veritatis et quasi architecto beatae vitae dicta sunt explicabo. Nemo enim sed quia consequuntur magni dolores eos qui ratione voluptatem sequi nesciunt.</p>
</section>

<section class="highlights">
  <div class="circle dark left">
    <svg width="96" height="90" viewBox="0 0 96 90" fill="none" stroke="#fff" stroke-width="3"><circle cx="22" cy="12" r="7"/><circle cx="74" cy="12" r="7"/><circle cx="48" cy="40" r="6"/><path d="M10 40c0-10 6-18 12-18s12 8 12 18v10M62 50V40c0-10 6-18 12-18s12 8 12 18"/><path d="M40 62c0-8 4-12 8-12s8 4 8 12v24M4 50l18 30h14M92 50L74 80H60"/></svg>
    JUDICIAL DEFENSE<br>IN CIVIL MATTERS
  </div>
  <div class="circle gold">
    <svg width="104" height="96" viewBox="0 0 104 96" fill="none" stroke="#fff" stroke-width="3"><rect x="3" y="3" width="98" height="68" rx="4"/><rect x="11" y="11" width="82" height="52"/><path d="M40 71v16M64 71v16M28 90h48M18 30l14 10 10-8 16 14M66 22h20M66 32h20M66 42h20M66 52h20"/></svg>
    BANKRUPTCY &amp;<br>REORGANIZATION OF<br>COMPANIES
  </div>
  <div class="circle dark right">
    <svg width="70" height="82" viewBox="0 0 70 82" fill="none" stroke="#fff" stroke-width="3"><path d="M3 3h46l18 18v58H3z"/><path d="M49 3v18h18M16 52h40M16 62h40M30 26h26M30 36h26"/><path d="M20 18c-6 0-8 4-6 7s8 3 9 6-2 7-6 7M16 14v30"/></svg>
    FINANCIAL &amp; TAX<br>ADVICE
  </div>
</section>

<section class="services">
  <h2 class="section-title">OUR SERVICES</h2>
  <span class="rule"></span>
  <div class="service" style="left:111px;top:154px">
    <div class="icon"><svg width="54" height="60" viewBox="0 0 54 60" fill="none" stroke="#fff" stroke-width="2.5"><path d="M6 6h38v48H6z"/><path d="M14 18h22M14 26h22M14 34h22M14 42h12"/><circle cx="40" cy="46" r="5"/></svg></div>
    <div class="body"><h3>Commercial &amp; Corporate<br>Law Advisory</h3><p>Sed ut perspiciatis unde omnis iste natus err or sit voluptatem accusantium</p></div>
  </div>
  <div class="service" style="left:651px;top:156px">
    <div class="icon"><svg width="56" height="60" viewBox="0 0 56 60" fill="none" stroke="#fff" stroke-width="2.5"><path d="M12 4h32M8 12h40M4 20h48l-6 36H10z"/><circle cx="28" cy="36" r="7"/></svg></div>
    <div class="body"><h3>Collection and recovery of assets</h3><p>Sed ut perspiciatis unde omnis iste natus err or sit voluptatem accusantium</p></div>
  </div>
  <div class="service" style="left:111px;top:335px">
    <div class="icon"><svg width="62" height="58" viewBox="0 0 62 58" fill="none" stroke="#fff" stroke-width="2.5"><circle cx="14" cy="8" r="6"/><circle cx="48" cy="8" r="6"/><circle cx="31" cy="28" r="5"/><path d="M4 40V24c0-6 4-8 10-8s10 2 10 8v16M38 40V24c0-6 4-8 10-8s10 2 10 8v16M24 56V42c0-4 3-6 7-6s7 2 7 6v14M10 40v16M18 40v16M44 40v16M52 40v16"/></svg></div>
    <div class="body"><h3>Legal defense in civil, criminal, labor and family matters</h3><p>Sed ut perspiciatis unde omnis iste natus err or sit voluptatem accusantium</p></div>
  </div>
  <div class="service" style="left:651px;top:337px">
    <div class="icon"><svg width="52" height="60" viewBox="0 0 52 60" fill="none" stroke="#fff" stroke-width="2.5"><path d="M26 3l21 8v18c0 14-10 24-21 28C15 53 5 43 5 29V11z"/><circle cx="26" cy="30" r="12"/><path d="M30 25c-2-2-8-2-8 1s8 3 8 6-6 3-8 1M26 20v20"/></svg></div>
    <div class="body"><h3>Asset protection</h3><p>Sed ut perspiciatis unde omnis iste natus err or sit voluptatem accusantium</p></div>
  </div>
</section>

<section class="blog">
  <h2 class="section-title">LATEST <em>BLOG</em></h2>
  <span class="rule"></span>
  <article class="post" style="left:111px">
    <div class="photo" role="img" aria-label="Two people reviewing a contract on a desk"></div>
    <div class="card"><div class="date">09 AUGUST 2021</div><h4>SED UT PERSPICIATIS UNDE</h4><p>Nemo enim ipsam voluptatem quiaer voluptas sit aspernatur aut odit aut fugit enim consequuntur magni</p></div>
  </article>
  <article class="post" style="left:444px">
    <div class="photo" role="img" aria-label="Business handshake across a meeting table"></div>
    <div class="card"><div class="date">09 AUGUST 2021</div><h4>SED UT PERSPICIATIS UNDE</h4><p>Nemo enim ipsam voluptatem quiaer voluptas sit aspernatur aut odit aut fugit enim consequuntur magni</p></div>
  </article>
  <article class="post" style="left:777px">
    <div class="photo" role="img" aria-label="Professional woman sitting at an office desk"></div>
    <div class="card"><div class="date">09 AUGUST 2021</div><h4>SED UT PERSPICIATIS UNDE</h4><p>Nemo enim ipsam voluptatem quiaer voluptas sit aspernatur aut odit aut fugit enim consequuntur magni</p></div>
  </article>
</section>

<section class="how">
  <div class="photo" role="img" aria-label="Team of lawyers in a bright meeting room discussing a case"></div>
  <div class="content">
    <h2 class="section-title">HOW <em>WE WORK</em></h2>
    <span class="rule"></span>
    <p>Sed ut perspiciatis unde omnis iste natus error sit voluptatem accusantium doloremque laudantium, totam rem aperiam, eaque ipsa quae ab illo inventore veritatis et quasi architecto beatae vitae dicta sunt explicabo. Nemo enim ipsam voluptatem quia voluptas sit aspernatur aut odit aut fugit, sed quia consequuntur magni dolores eos qui ratione voluptatem sequi nesciunt. Neque porro quisquam est, qui dolorem ipsum quia dolor sit amet, consectetur, adipisci velit, sed quia non numquam eius modi et dolore magnam aliquam quaerat voluptatem.</p>
    <a class="btn" href="#">READ MORE</a>
  </div>
</section>

<footer class="site-footer">
  <div class="brand">
    <div class="brand-mark"></div>
    <div><div class="brand-name">Berrocal Tizón</div><div class="brand-sub">ABOGADOS Y CONSULTORES</div></div>
  </div>
  <nav class="footer-nav">
    <a href="#">HOME</a><a href="#">ABOUT US</a><a href="#">SERVICES</a><a href="#">HOW WE WORK</a><a href="#">BLOG</a><a href="#">FAQ</a><a href="#">CONTACT</a>
  </nav>
  <div class="social" aria-label="Social links"><span></span><span></span><span></span><span></span><span></span></div>
  <p class="copyright">© Copyrights 2021 - Berrocal Tizón.All Rights Reserved.</p>
</footer>

</body>
</html>
```